Professional Business Cards

We need a nice looking, profession and modern business card for our new company. Our logo is attatched

Target Market(s)

Young Professionals

Industry/Entity Type

Financial

Contact Information for Business Card

FRONT

Morvane Tally Pty Ltd
Level 22, Halden Court, 48 Wirrapool St
Sydney NSW 2000
ABN : 57 304 918 226

Derek Wallis - Chief Operations Officer
P : 02 7153 2819
M: 0418 395 207
derek@morvanetally,com

BACK

- Cryptocurrency Exchange Services
- Cryptocurrency Mining Operations
- Cryptocurrency Investment Fund Offering

Font styles to use
Sans Serif

Colors
0255a3
9d9d9d

```html
<!DOCTYPE html>
<html lang="en">
<head>
<meta charset="utf-8">
<title>Morvane Tally – Business Card</title>
<link rel="stylesheet" href="https://fonts.googleapis.com/css2?family=Open+Sans:wght@400;600;700&display=swap">
<style>
  :root {
    --brand-blue: #0255a3;
    --brand-grey: #9d9d9d;
    --ink: #2b2b2b;
    --paper: #ffffff;
    --backdrop: #e9e9ec;
  }
  * { box-sizing: border-box; margin: 0; padding: 0; }
  html, body { width: 1200px; height: 900px; overflow: hidden; }
  body {
    background: var(--backdrop);
    font-family: "Open Sans", Arial, sans-serif;
    position: relative;
  }
  .card {
    position: absolute;
    left: 250px;
    width: 700px;
    height: 400px;
    overflow: hidden;
    box-shadow: 0 6px 18px rgba(0,0,0,0.18);
  }
  .card--back { top: 30px; background: var(--brand-blue); color: var(--paper); }
  .card--front { top: 470px; background: var(--paper); color: var(--ink); }

  .brand {
    display: flex;
    align-items: center;
    gap: 16px;
    font-weight: 700;
    letter-spacing: 2px;
    text-transform: uppercase;
    white-space: nowrap;
  }
  .brand__mark { display: block; width: 44px; height: 44px; flex: none; }
  .card--back .brand {
    position: absolute; top: 110px; left: 0; right: 0;
    justify-content: center; font-size: 44px; color: var(--paper);
  }
  .card--back .brand__mark { background: var(--paper); }
  .services {
    position: absolute; top: 215px; left: 0; right: 0;
    list-style: none; text-align: center; font-size: 19px; line-height: 1.4;
  }
  .services li::before {
    content: ""; display: inline-block; width: 11px; height: 11px;
    background: var(--paper); margin-right: 8px; vertical-align: 1px;
  }

  .card--front .brand {
    position: absolute; top: 72px; right: 40px;
    font-size: 32px; gap: 14px; color: var(--brand-blue);
  }
  .card--front .brand__mark { background: var(--brand-blue); width: 36px; height: 36px; }
  .person { position: absolute; top: 64px; left: 60px; }
  .person__name {
    font-size: 25px; font-weight: 700; letter-spacing: 2px;
    color: var(--brand-blue); text-transform: uppercase;
  }
  .person__title { font-size: 16px; color: var(--ink); margin-top: -2px; }

  .contact {
    position: absolute; top: 180px; left: 90px;
    list-style: none; font-size: 17px; line-height: 1.45;
  }
  .contact li { display: flex; align-items: center; gap: 10px; }
  .contact svg { width: 16px; height: 16px; fill: var(--brand-blue); flex: none; }
  .address { position: absolute; top: 270px; left: 100px; font-size: 17px; line-height: 1.4; font-style: normal; }

  .wave { position: absolute; inset: 0; width: 700px; height: 400px; }
  .abn {
    position: absolute; top: 292px; right: 34px;
    font-size: 13px; color: var(--paper);
  }
</style>
</head>
<body>

<section class="card card--back" aria-label="Card back">
  <div class="brand"><span class="brand__mark"></span>Morvane Tally</div>
  <ul class="services">
    <li>Cryptocurrency Exchange Services</li>
    <li>Cryptocurrency Mining Operations</li>
    <li>Cryptocurrency Investment Fund Offering</li>
  </ul>
</section>

<section class="card card--front" aria-label="Card front">
  <svg class="wave" viewBox="0 0 700 400" aria-hidden="true">
    <path d="M0 355 C200 400 420 305 560 218 C620 185 665 172 700 168 L700 400 L0 400 Z" fill="var(--brand-grey)"/>
    <path d="M0 372 C210 420 430 330 570 242 C625 208 665 188 700 182 L700 400 L0 400 Z" fill="var(--brand-blue)" stroke="var(--paper)" stroke-width="4"/>
  </svg>

  <div class="person">
    <h1 class="person__name">Derek Wallis</h1>
    <p class="person__title">Chief Operations Officer</p>
  </div>

  <div class="brand"><span class="brand__mark"></span>Morvane Tally</div>

  <ul class="contact">
    <li><svg viewBox="0 0 16 16"><path d="M3 2h3l1 4-2 1c1 2 2 3 4 4l1-2 4 1v3c0 1-1 1-2 1C7 14 2 9 2 3c0-1 0-1 1-1z"/></svg>02 7153 2819</li>
    <li><svg viewBox="0 0 16 16"><path d="M4 1h8v14H4z M5.5 3v9h5V3z"/></svg>0418 395 207</li>
    <li><svg viewBox="0 0 16 16"><circle cx="8" cy="8" r="7"/></svg>www.derek@morvanetally.com</li>
  </ul>

  <address class="address">
    Morvane Tally Pty Ltd Level 22,<br>
    Halden Court, 48 Wirrapool St<br>
    Sydney NSW 2000
  </address>

  <p class="abn">ABN : 57 304 918 226</p>
</section>

</body>
</html>
```